Tallyleaf Web Design

Create Website Design for Tallyleaf. Tallyleaf is online application for collaboration team work system (task list management). More concept design for this project please find attach file ("tallyleaf website concept.pdf") . But my concept is just describe minimal features not bind design

For tallyleaf logo, i had already attach files. But i had not decided what color i chose, so it's okay if you suggest logo color for your suitable website design.
Updates

Dear All Designer,

I like brisk carousel (http://quorvanlabs.example/brisk-carousel/),
may be your concept design can adjust with this concept.
but don't worry about script for brisk carousel, my team will be handle
You just make website design to suitable with brisk carousel

but if you had own website design concept are welcome

thanks

Target Market(s)

Business Company

Industry/Entity Type

Management

```html
<!DOCTYPE html>
<html lang="en">
<head>
<meta charset="utf-8">
<title>Tallyleaf – Online Collaboration Team Work</title>
<link href="https://fonts.googleapis.com/css2?family=PT+Sans:ital,wght@0,400;0,700;1,400;1,700&family=Varela+Round&display=swap" rel="stylesheet">
<style>
  :root {
    --header-top: #dedede;
    --header-bottom: #cfcfcf;
    --logo-grey: #7d7d7d;
    --nav-bg: #f4f4f4;
    --nav-border: #a9a9a9;
    --ink: #1e1e1e;
    --hero-dark: #121212;
    --hero-mid: #3b3b3b;
    --white: #ffffff;
    --muted: #d7d7d7;
    --button-top: #2d78c0;
    --button-bottom: #0d3f78;
    --footer-dark: #1b1b1b;
    --footer-mid: #474747;
  }
  * { box-sizing: border-box; margin: 0; padding: 0; }
  html, body { width: 1200px; height: 1042px; overflow: hidden; }
  body { position: relative; font-family: "PT Sans", Arial, sans-serif; color: var(--ink); background: var(--white); }

  .site-header { position: absolute; left: 0; top: 0; width: 1200px; height: 129px;
    background: linear-gradient(var(--header-top), var(--header-bottom)); }
  .brand { position: absolute; left: 84px; top: 22px; display: flex; align-items: center; gap: 12px; }
  .brand-name { font-family: "Varela Round", "PT Sans", sans-serif; font-size: 64px; color: var(--logo-grey); line-height: 1; }
  .brand-dot { width: 26px; height: 26px; border-radius: 50%; background: var(--logo-grey); }

  .main-nav { position: absolute; left: 447px; top: 49px; width: 467px; height: 35px;
    border: 1px solid var(--nav-border); border-radius: 18px; background: var(--nav-bg);
    box-shadow: inset 0 -2px 3px rgba(0,0,0,.08); }
  .main-nav a { position: absolute; top: 7px; font-size: 15px; font-style: italic; color: var(--ink); text-decoration: none; }

  .login-form label { position: absolute; left: 960px; width: 42px; text-align: right; font-size: 12px; font-style: italic; color: #333; }
  .login-form .field { position: absolute; left: 1005px; width: 117px; height: 29px; border: 1px solid #aaa;
    border-radius: 3px; background: linear-gradient(#f2f2f2, #fbfbfb); }

  .hero { position: absolute; left: 0; top: 129px; width: 1200px; height: 612px;
    background: radial-gradient(ellipse 70% 80% at 55% 30%, var(--hero-mid), var(--hero-dark)); }

  .slider { position: absolute; left: 66px; top: 43px; width: 657px; height: 506px; border-radius: 6px; overflow: hidden;
    box-shadow: 0 0 0 1px #555, 0 4px 14px rgba(0,0,0,.6); }
  .slide-photo { position: absolute; inset: 0;
    background: linear-gradient(100deg, #f1f1f1 0%, #d8d8d8 35%, #3a3a44 60%, #2b2020 100%); }
  .slide-shade { position: absolute; left: 0; right: 0; bottom: 0; height: 290px;
    background: linear-gradient(rgba(0,0,0,0), rgba(0,0,0,.75) 45%, rgba(0,0,0,.85)); }
  .slide-title { position: absolute; left: 21px; top: 270px; font-size: 64px; font-weight: 700; color: var(--white); letter-spacing: -1px; }
  .slide-sub { position: absolute; left: 21px; top: 344px; font-size: 19px; font-weight: 700; color: var(--white); }
  .slide-caption-title { position: absolute; left: 21px; top: 390px; font-size: 25px; font-weight: 700; font-style: italic; color: var(--white); }
  .slide-caption { position: absolute; left: 21px; top: 423px; width: 600px; font-size: 14px; line-height: 23px; font-weight: 700; font-style: italic; color: var(--white); }
  .read-more { position: absolute; left: 504px; top: 462px; width: 121px; height: 31px; border-radius: 16px;
    border: 1px solid #6fa8dc; background: linear-gradient(var(--button-top), var(--button-bottom));
    color: var(--white); font-size: 16px; font-weight: 700; font-style: italic; text-align: center; line-height: 29px; }
  .slider-dots { position: absolute; left: 19px; top: 479px; display: flex; gap: 6px; }
  .slider-dots span { width: 14px; height: 14px; border-radius: 50%; border: 2px solid #888; background: #444; }

  .hero-headline { position: absolute; left: 740px; top: 68px; font-size: 72px; line-height: 58px; font-weight: 700; font-style: italic; color: var(--white); letter-spacing: -1px; }
  .hero-text { position: absolute; left: 741px; top: 333px; width: 428px; font-size: 13.5px; line-height: 23.6px; font-style: italic; color: var(--muted); }

  .features { position: absolute; left: 0; top: 741px; width: 1200px; height: 201px; background: var(--white); }
  .feature { position: absolute; top: 28px; width: 380px; height: 165px; }
  .feature h3 { font-size: 15px; font-weight: 700; font-style: italic; color: var(--ink); }
  .feature-icon { position: absolute; left: 2px; top: 40px; width: 66px; height: 68px; border-radius: 8px; }
  .icon-tools { background: linear-gradient(#d9b65a, #b9b9b9 55%, #8f8f8f); }
  .icon-sync { background: linear-gradient(#6bb3e8, #2a7fc4); }
  .icon-report { background: linear-gradient(#f1f1f1, #cfcfcf); }
  .feature p { position: absolute; top: 37px; width: 258px; font-size: 13px; line-height: 19.5px; font-style: italic; color: var(--ink); }

  .site-footer { position: absolute; left: 0; top: 942px; width: 1200px; height: 100px;
    background: linear-gradient(var(--footer-dark), var(--footer-mid) 70%, #2a2a2a); }
  .footer-nav { position: absolute; left: 120px; top: 42px; font-size: 15px; font-style: italic; color: var(--muted); word-spacing: 4px; }
</style>
</head>
<body>
  <header class="site-header">
    <div class="brand"><span class="brand-name">tallyleaf</span><span class="brand-dot"></span></div>
    <nav class="main-nav">
      <a style="left:38px">Home</a><a style="left:108px">Link</a><a style="left:167px">Link</a>
      <a style="left:225px">Link</a><a style="left:283px">Link</a><a style="left:342px">Link</a><a style="left:400px">Link</a>
    </nav>
    <form class="login-form">
      <label style="top:40px">User</label><span class="field" style="top:34px"></span>
      <label style="top:79px">Login</label><span class="field" style="top:72px"></span>
    </form>
  </header>

  <section class="hero">
    <div class="slider">
      <div class="slide-photo" role="img" aria-label="Photo of a presenter at a whiteboard with business charts, audience in the foreground"></div>
      <div class="slide-shade"></div>
      <h2 class="slide-title">About Tallyleaf</h2>
      <p class="slide-sub">Who we are what we do...</p>
      <h3 class="slide-caption-title">Application</h3>
      <p class="slide-caption">Aenean sit amet lectus at enim luctus semper. Phasellus gravida tempor eros, sed aliquam nisi pellentesque ac. Nunc id risus mi. Etiam eu nisl neque, ut adipiscing diam.</p>
      <a class="read-more">Read More</a>
      <div class="slider-dots"><span></span><span></span><span></span><span></span></div>
    </div>
    <h1 class="hero-headline">Customize<br>Online<br>Collaboration<br>Team Work</h1>
    <p class="hero-text">Donec et eros consectetur tortor accumsan porttitor. Proin scelerisque, mi ut rhoncus sodales, tellus ante convallis odio, id gravida turpis felis vel magna. Class aptent taciti sociosqu ad litora torquent per conubia nostra, per inceptos himenaeos. Sed varius, leo et egestas malesuada, diam ipsum hendrerit nisl, eu tincidunt erat nunc vel odio. Quisque aliquet aliquam leo, ac dapibus felis mattis ac. Sed blandit elementum consequat. Sed eget quam eget lorem eleifend cursus. Morbi vestibulum suscipit sodales. Suspendisse dapibus lacus non mi elementum at viverra lectus condimentum. Mauris bibendum est et.</p>
  </section>

  <section class="features">
    <article class="feature" style="left:72px">
      <h3>Customize Application</h3>
      <div class="feature-icon icon-tools" role="img" aria-label="Illustration of a desk cup holding pencils and a ruler"></div>
      <p style="left:75px">Lorem ipsum dolor sit amet, consectetur adipiscing elit. In porta nunc iaculis est interdum aliquam. Donec et eros consectetur tortor accumsan porttitor. Proin scelerisque, mi ut rhoncus sodales, tellus ante,</p>
    </article>
    <article class="feature" style="left:450px">
      <h3>Synchronize All Device</h3>
      <div class="feature-icon icon-sync" role="img" aria-label="Illustration of a cloud for device synchronisation"></div>
      <p style="left:87px">Lorem ipsum dolor sit amet, consectetur adipiscing elit. In porta nunc iaculis est interdum aliquam. Donec et eros consectetur tortor accumsan porttitor. Proin scelerisque, mi ut rhoncus sodales, tellus ante,</p>
    </article>
    <article class="feature" style="left:828px">
      <h3>Report</h3>
      <div class="feature-icon icon-report" role="img" aria-label="Illustration of a report document with a chart"></div>
      <p style="left:82px">Lorem ipsum dolor sit amet, consectetur adipiscing elit. In porta nunc iaculis est interdum aliquam. Donec et eros consectetur tortor accumsan porttitor. Proin scelerisque, mi ut rhoncus sodales, tellus ante,</p>
    </article>
  </section>

  <footer class="site-footer">
    <nav class="footer-nav">Home | Link | Link | Link | Link | Link | Link</nav>
  </footer>
</body>
</html>
```